International e-commerce business needs packaging design

We need a design that can be printed onto clear/see through Polypropylene bags to advertise our products and brand (We sell Electronic accessories such as cables and adapters but are expanding into other areas as well).
The bags we will be using will be of varying sizes ranging from roughly 15cm x 15cm up to 40cm x 40cm
We have attached a file (example 1 file) that show what we consider a good example of the sort of design we are looking for.
We would also like to have a new company logo as well though this is not critical so if someone comes up with a good alternative to our current design (also attached) we are more likely to choose a designer who comes up with a logo as well.
We are open to a complete revamp of the logo but we do want to keep the colour theme of rich red & grey/silver and also its shape (roughly).
In terms of details required in the packaging design there are a couple of things we require which should be straight forward enough...
1) Logo to be positioned top left (similar to example 1 file)
2) We need a "BLANK" white box suitable for affixing barcodes (similar to example 1 file) located bottom right area.
3) We need a safety warning along the very bottom warning of suffocation. The wording should read...
WARNING - risk of suffocation. Keep away from young children.
4) The colour theme should be rich red (like our current logo) and silvers/greys
5) In example 1 design the top right has the repeating words "computer accessories". We require another blank white box for us to put our own product descriptions in.
6) somewhere on the bag it should say our company name "Lumen Trove" with the "Registered" trademark logo on the end.
Thanks in advance to anyone who puts forward a design.
*UPDATE* We'd like to see binary code used within any design and have the below binary code which represents "Lumen Trove". It would be nice to incorporate this possibly in the logo but if not then certainly on any packaging design...
01001100 01110101 01101101 01100101 01101110 00100000 01010100 01110010 01101111 01110110 01100101
E-Commerce
- Calibri or Verdana

```html
<!DOCTYPE html>
<html lang="en">
<head>
<meta charset="utf-8">
<title>Lumen Trove – Packaging Bag</title>
<link rel="stylesheet" href="https://fonts.googleapis.com/css2?family=Carlito:wght@400;700&display=swap">
<style>
  :root {
    --red: #c8102e;
    --red-deep: #7d0a1a;
    --ink: #141414;
    --silver: #d9d9d9;
    --grey: #6e6e6e;
    --film: #f4f5f6;
    --white: #ffffff;
  }
  * { margin: 0; padding: 0; box-sizing: border-box; }
  html, body { width: 841px; height: 1200px; overflow: hidden; background: var(--white); }
  body { font-family: "Carlito", "Calibri", sans-serif; }
  .bag { position: relative; width: 841px; height: 1200px; background: var(--film); overflow: hidden; }

  .header-strip { position: absolute; left: 0; top: 0; width: 841px; height: 150px; background: var(--white); }
  .hang-hole { position: absolute; left: 385px; top: 50px; width: 72px; height: 24px; border-radius: 12px; border: 2px solid var(--silver); background: var(--film); }

  .brand-band { position: absolute; left: 0; top: 150px; width: 841px; height: 202px;
    background: linear-gradient(180deg, var(--red) 0%, #a90d25 70%, var(--red-deep) 100%); overflow: hidden; }
  .brand-art { position: absolute; right: 0; top: 0; width: 300px; height: 202px;
    background: linear-gradient(120deg, rgba(255,255,255,0) 0%, rgba(255,255,255,0.15) 45%, rgba(255,255,255,0.35) 100%); }
  .brand-name { position: absolute; left: 42px; top: 95px; font-size: 60px; line-height: 1; font-weight: 400; color: var(--ink); letter-spacing: -1px; white-space: nowrap; }
  .brand-name sup { font-size: 24px; vertical-align: top; position: relative; top: 4px; margin-left: 2px; }
  .binary-line { position: absolute; left: 42px; top: 168px; width: 500px; font-size: 11.5px; line-height: 1.2; font-weight: 400; color: rgba(255,255,255,0.8); letter-spacing: 0.3px; white-space: nowrap; }

  .category-band { position: absolute; left: 0; top: 352px; width: 841px; height: 58px; background: var(--ink);
    display: flex; align-items: center; justify-content: center; }
  .category-line { color: var(--white); font-size: 31px; font-weight: 700; letter-spacing: 0.2px; white-space: nowrap; }

  .description-box { position: absolute; left: 502px; top: 841px; width: 274px; height: 68px; background: #eef0f0; border: 2px solid var(--silver); }

  .barcode-panel { position: absolute; left: 0; top: 1005px; width: 841px; height: 155px;
    background: linear-gradient(90deg, rgba(20,20,20,0) 0%, rgba(20,20,20,0.6) 35%, var(--ink) 55%); }
  .barcode-box { position: absolute; left: 494px; top: 1022px; width: 280px; height: 122px; background: var(--white); border: 3px solid var(--ink); }

  .brand-seal { position: absolute; left: 85px; top: 805px; width: 310px; height: 310px; }
  .seal-name { position: absolute; left: 85px; top: 940px; width: 310px; text-align: center; color: var(--white); font-size: 32px; line-height: 1; font-weight: 400; white-space: nowrap; }
  .seal-name sup { font-size: 14px; vertical-align: top; }

  .warning-bar { position: absolute; left: 0; top: 1160px; width: 841px; height: 40px; background: var(--ink);
    display: flex; align-items: center; padding-left: 30px; }
  .warning-text { color: var(--white); font-size: 16px; font-weight: 700; white-space: nowrap; }
</style>
</head>
<body>
  <main class="bag">
    <div class="header-strip"><div class="hang-hole"></div></div>

    <section class="brand-band">
      <div class="brand-art" role="img" aria-label="Decorative pattern of red and white tiles"></div>
      <div class="brand-name">Lumen Trove<sup>®</sup></div>
      <p class="binary-line">01001100 01110101 01101101 01100101 01101110 00100000 01010100 01110010 01101111 01110110 01100101</p>
    </section>

    <section class="category-band">
      <p class="category-line">Cables - Adapters - Electronic Accessories - Consumables</p>
    </section>

    <div class="description-box" aria-label="Product description area"></div>

    <div class="barcode-panel"></div>

    <svg class="brand-seal" viewBox="0 0 310 310" aria-hidden="true">
      <circle cx="155" cy="155" r="153" fill="#3a3a3a" stroke="#d9d9d9" stroke-width="3"/>
    </svg>
    <div class="seal-name">Lumen Trove<sup>®</sup></div>

    <div class="barcode-box" aria-label="Barcode label area"></div>

    <footer class="warning-bar">
      <p class="warning-text">WARNING - Risk of suffocation. Keep away from young children.</p>
    </footer>
  </main>
</body>
</html>
```